Renata Quisby

Luxury And Style -

Black - White & Gold

Target Market(s)

Fashion

Industry/Entity Type

Fashion

Requirements
Must have
• High-End
Nice to have
• We will Print on Silk Paper

```html
<!DOCTYPE html>
<html lang="en">
<head>
<meta charset="utf-8">
<title>Renata Quisby — Folder and Letterhead</title>
<link href="https://fonts.googleapis.com/css2?family=Josefin+Sans:wght@300&family=Arimo:wght@400&display=swap" rel="stylesheet">
<style>
  :root {
    --ink: #1f1f1f;
    --paper: #ffffff;
    --gold: #d4ad3c;
    --gold-deep: #b8891f;
    --gold-light: #fbe89a;
    --frame: #6b6b6b;
    --text: #2a2a2a;
  }
  * { margin: 0; padding: 0; box-sizing: border-box; }
  html, body {
    width: 1200px; height: 834px; overflow: hidden;
    background: var(--paper);
  }
  .sheet { position: relative; width: 1200px; height: 834px; }

  .cover {
    position: absolute; left: 32px; top: 23px; width: 562px; height: 795px;
    background: var(--ink);
  }
  .letterhead {
    position: absolute; left: 608px; top: 23px; width: 562px; height: 795px;
    background: var(--paper);
    border: 1px solid var(--frame);
    box-shadow: 2px 0 1px -1px #9a9a9a;
  }

  .brand { position: absolute; left: 0; right: 0; text-align: center; }
  .brand-mark {
    display: block; margin: 0 auto;
    border: 1.5px solid var(--gold); border-radius: 50%;
  }
  .brand-name {
    display: block;
    font-family: "Josefin Sans", sans-serif; font-weight: 300;
    color: var(--gold); white-space: nowrap;
    text-transform: uppercase;
  }
  .brand-tagline {
    display: block;
    font-family: "Josefin Sans", sans-serif; font-weight: 300;
    color: var(--gold); text-transform: uppercase; white-space: nowrap;
  }

  .cover .brand { top: 335px; }
  .cover .brand-mark { width: 62px; height: 62px; margin-bottom: 22px; }
  .cover .brand-name { font-size: 21px; letter-spacing: 5.5px; padding-left: 5.5px; }
  .cover .brand-tagline { font-size: 12px; letter-spacing: 0.6px; margin-top: 8px; }

  .letterhead .brand { top: 58px; }
  .letterhead .brand-mark { width: 34px; height: 34px; margin-bottom: 14px; }
  .letterhead .brand-name { font-size: 12.5px; letter-spacing: 3.2px; padding-left: 3.2px; }
  .letterhead .brand-tagline { font-size: 7px; letter-spacing: 0.3px; margin-top: 4px; }

  .footer-rule {
    position: absolute; left: 46px; width: 469px; top: 717px; height: 4px;
    background: linear-gradient(90deg, var(--gold-deep), var(--gold-light) 50%, var(--gold-deep));
  }
  .contact-row {
    position: absolute; left: 0; right: 0; top: 733px;
    display: flex; justify-content: center; align-items: center;
    font-family: "Arimo", sans-serif; font-size: 6.3px; letter-spacing: 1.6px;
    color: var(--text); text-transform: uppercase;
  }
  .contact-item { display: flex; align-items: center; gap: 4px; padding: 0 6px; }
  .contact-item + .contact-item { border-left: 0.8px solid var(--text); }
  .contact-item svg { width: 8px; height: 8px; flex: none; }
</style>
</head>
<body>
<div class="sheet">

  <section class="cover">
    <div class="brand">
      <span class="brand-mark"></span>
      <span class="brand-name">Renata Quisby</span>
      <span class="brand-tagline">Luxury and Style</span>
    </div>
  </section>

  <section class="letterhead">
    <div class="brand">
      <span class="brand-mark"></span>
      <span class="brand-name">Renata Quisby</span>
      <span class="brand-tagline">Luxury and Style</span>
    </div>

    <div class="footer-rule"></div>

    <div class="contact-row">
      <span class="contact-item">
        <svg viewBox="0 0 10 10"><path d="M8.5 1 L7 0.5 L6 3 L7 3.8 Q6 6.5 3.8 7 L3 6 L0.8 7 L1.2 8.7 Q5.5 9.5 8.5 1Z" fill="var(--text)"/></svg>
        +00-0000-0000-000
      </span>
      <span class="contact-item">
        <svg viewBox="0 0 10 10"><rect x="0.7" y="2" width="8.6" height="6" fill="none" stroke="var(--text)" stroke-width="0.9"/><path d="M0.7 2 L5 5.5 L9.3 2" fill="none" stroke="var(--text)" stroke-width="0.9"/></svg>
        info@companyname.com
      </span>
      <span class="contact-item">
        <svg viewBox="0 0 10 10"><circle cx="5" cy="5" r="4.3" fill="none" stroke="var(--text)" stroke-width="0.8"/><ellipse cx="5" cy="5" rx="1.9" ry="4.3" fill="none" stroke="var(--text)" stroke-width="0.7"/><path d="M0.7 5 H9.3 M1.4 2.8 H8.6 M1.4 7.2 H8.6" stroke="var(--text)" stroke-width="0.6"/></svg>
        www.companyname.com
      </span>
    </div>
  </section>

</div>
</body>
</html>
```